Brightwell Systems, a software development company, needs a website

We need a website to promote our software development company. The company is brand new and we want to market ourselves. We develop all kinds of software from web applications, to desktop applications, to mobile applications. Small company, not a lot of history, just need something flashy.

```html
<!DOCTYPE html>
<html lang="en">
<head>
<meta charset="utf-8">
<title>Brightwell Systems — Software Development</title>
<link href="https://fonts.googleapis.com/css2?family=Orbitron:wght@700;900&family=Roboto:wght@400;500;700&display=swap" rel="stylesheet">
<style>
:root{
  --navy:#1c2382;
  --navy-deep:#121a5e;
  --cyan:#21b4e6;
  --cyan-bright:#2ad0f5;
  --ink:#1a1a1a;
  --text:#2b2b2b;
  --muted:#666;
  --line:#e6e6e6;
  --footer:#1e1e20;
  --white:#fff;
}
*{box-sizing:border-box;margin:0;padding:0}
html,body{width:1200px;height:4453px;overflow:hidden;background:var(--white)}
body{position:relative;font-family:"Roboto",Arial,sans-serif;color:var(--text)}
.abs{position:absolute}
.display{font-family:"Orbitron","Roboto",sans-serif;font-weight:900;letter-spacing:2px;text-transform:uppercase}
.c-navy{color:var(--navy)} .c-cyan{color:var(--cyan)}
.btn{position:absolute;height:55px;border-radius:28px;color:#fff;font-weight:700;font-size:19px;display:flex;align-items:center;justify-content:center;gap:10px}
.btn svg{width:18px;height:18px}
.btn-cyan{background:var(--cyan)} .btn-navy{background:var(--navy)}

/* header */
.header{left:0;top:0;width:1200px;height:135px;background:#fff;border-bottom:1px solid var(--line)}
.brand{left:86px;top:22px;display:flex;align-items:center;gap:14px}
.brand-dot{width:80px;height:80px;border-radius:50%;background:var(--cyan)}
.brand-name{font-size:28px;line-height:1.3;color:var(--navy)}
.brand-name span{display:block;color:var(--cyan)}
.contact-item{top:22px;display:flex;gap:10px;align-items:center;font-size:13px}
.contact-item .ic{width:48px;height:48px;border-radius:50%;background:var(--cyan);display:flex;align-items:center;justify-content:center}
.contact-item b{display:block;color:var(--navy);font-weight:700;font-size:14px}
.nav{top:92px;left:480px;display:flex;gap:31px;font-size:18px;color:var(--ink)}

/* hero */
.hero{left:0;top:135px;width:1200px;height:680px;background:linear-gradient(110deg,#0a1a55 0%,#123a8f 40%,#1a8fd6 75%,#2de0f5 100%)}
.hero-brand{left:836px;top:300px;width:230px;text-align:center;color:#fff;font-size:27px;line-height:1.45}
.hero-brand .hero-dot{width:100px;height:100px;border-radius:50%;background:rgba(255,255,255,.9);margin:0 auto 34px}
.svc{position:absolute;border-radius:50%;display:flex;flex-direction:column;align-items:center;justify-content:center;text-align:center;color:#fff;font-size:16px;line-height:1.5}
.svc svg{margin-bottom:14px}
.svc-web{left:263px;top:643px;width:200px;height:200px;background:var(--navy-deep)}
.svc-mob{left:735px;top:643px;width:200px;height:200px;background:var(--cyan)}
.svc-desk{left:467px;top:622px;width:266px;height:266px;background:#fff;border:8px solid #d8d8d8;color:var(--navy);font-size:27px;line-height:1.4}
.svc-desk span{color:var(--cyan)}

/* welcome */
.section-title{position:absolute;left:0;width:1200px;text-align:center;font-size:29px;color:var(--ink)}
.lead{position:absolute;left:110px;width:980px;text-align:center;font-size:15.5px;line-height:36px;color:var(--ink)}
.divider{left:90px;top:1284px;width:1020px;height:1px;background:var(--line)}

/* focus */
.ring{position:absolute;border-radius:50%;border:7px solid var(--cyan);padding:10px}
.ring .photo{width:100%;height:100%;border-radius:50%}
.focus-title{left:583px;top:1420px;font-size:28px;color:var(--ink)}
.focus-text{left:583px;top:1470px;width:540px;font-size:15.5px;line-height:31px;color:var(--ink)}
.focus-list{left:583px;top:1537px;list-style:none;font-size:15.5px;color:var(--ink)}
.focus-list li{height:36px;display:flex;align-items:center;gap:12px}

/* what we do */
.band{left:0;top:1893px;width:1200px;height:752px;background:linear-gradient(180deg,#16207a 0%,#1646a8 55%,#1a70c8 100%)}
.wwd-title{left:90px;top:2118px;font-size:25px;color:#fff}
.wwd-text{left:90px;top:2162px;width:570px;font-size:15.5px;line-height:36px;color:#fff;text-align:justify}

/* blog */
.card{position:absolute;top:2788px;width:328px}
.card .img{height:194px;position:relative}
.card .date{position:absolute;left:14px;bottom:-8px;background:var(--cyan);color:#fff;font-size:13px;padding:6px 12px}
.card h3{margin-top:46px;font-size:16px;font-weight:500;color:var(--navy);letter-spacing:.3px}
.card p{margin-top:18px;font-size:11px;line-height:23px;color:var(--ink);text-align:justify}
.card a{display:block;margin-top:12px;font-size:15px;color:var(--cyan)}

/* clients */
.client{position:absolute;top:3376px;width:190px;height:83px;border:1px solid #ccc;display:flex;align-items:center;justify-content:center;gap:8px;font-weight:700;font-size:16px;color:#333}
.client i{width:12px;height:12px;background:#555;display:block}
.client.active{border-bottom:3px solid var(--navy)}
.arrow{position:absolute;top:3404px;font-size:26px;color:#888}

/* contact form */
.field{position:absolute;height:38px;border:1px solid #eee;border-bottom:3px solid #e3e3e3;background:#fff;font-size:12px;color:#555;display:flex;align-items:center;padding-left:16px;gap:6px}
.field.msg{align-items:flex-start;padding-top:12px}

/* footer */
.footer{left:0;top:4004px;width:1200px;height:449px;background:var(--footer)}
.foot-name{left:0;top:4288px;width:1200px;text-align:center;font-size:26px}
.foot-icon{position:absolute;top:4358px;width:84px;height:84px;border-radius:50%;background:var(--cyan);display:flex;align-items:center;justify-content:center}
</style>
</head>
<body>

<!-- Header -->
<header class="abs header">
  <div class="abs brand">
    <div class="brand-dot"></div>
    <div class="brand-name display">Brightwell<span>Systems</span></div>
  </div>
  <div class="abs contact-item" style="left:489px">
    <div class="ic"><svg width="24" height="24" viewBox="0 0 24 24" fill="#fff"><path d="M6.6 10.8a15 15 0 0 0 6.6 6.6l2.2-2.2c.3-.3.7-.4 1-.2 1.1.4 2.3.6 3.6.6.6 0 1 .4 1 1V20c0 .6-.4 1-1 1A17 17 0 0 1 3 4c0-.6.4-1 1-1h3.5c.6 0 1 .4 1 1 0 1.3.2 2.5.6 3.6.1.3 0 .7-.2 1z"/></svg></div>
    <div><b>Call Us</b>888 888 8888</div>
  </div>
  <div class="abs contact-item" style="left:659px">
    <div class="ic"><svg width="24" height="24" viewBox="0 0 24 24" fill="none" stroke="#fff" stroke-width="2"><rect x="3" y="5" width="18" height="14" rx="1"/><path d="M3 6l9 7 9-7"/></svg></div>
    <div><b>Email us</b>info@brightwellsystems.com</div>
  </div>
  <div class="abs contact-item" style="left:928px">
    <div class="ic"><svg width="24" height="24" viewBox="0 0 24 24" fill="none" stroke="#fff" stroke-width="2.4"><circle cx="10" cy="10" r="6"/><path d="M15 15l6 6"/></svg></div>
    <div><b>Search</b>Enter Search here...</div>
  </div>
  <nav class="abs nav"><span>Home</span><span>About Us</span><span>What We Do</span><span>Our Blog</span><span>Testimonials</span><span>Contact Us</span></nav>
</header>

<!-- Hero -->
<section class="abs hero" role="img" aria-label="Glowing laptop and smartphone showing software dashboards on a blue digital background"></section>
<svg class="abs" style="left:0;top:700px" width="1200" height="120" viewBox="0 0 1200 120">
  <path d="M0 110 Q600 -40 1200 110 L1200 120 L0 120Z" fill="#fff"/>
  <path d="M250 60 Q600 0 950 60" fill="none" stroke="var(--navy)" stroke-width="4"/>
</svg>
<div class="abs hero-brand display"><div class="hero-dot"></div>Brightwell<br>Systems</div>

<div class="svc svc-web">
  <svg width="64" height="60" viewBox="0 0 64 60" fill="none" stroke="#fff" stroke-width="3"><rect x="4" y="4" width="56" height="42" rx="2"/><path d="M4 14h56M22 56h20M32 46v10M12 22h14v14H12zM32 24h20M32 32h20"/></svg>
  Web<br>Applications
</div>
<div class="svc svc-mob">
  <svg width="36" height="64" viewBox="0 0 36 64" fill="none" stroke="#fff" stroke-width="3"><rect x="3" y="3" width="30" height="58" rx="4"/><path d="M13 54h10M12 24l6-6 6 6v10H12z"/></svg>
  Mobile<br>Applications
</div>
<div class="svc svc-desk">
  <svg width="90" height="64" viewBox="0 0 90 64" fill="none" stroke-width="3"><rect x="4" y="8" width="56" height="38" rx="2" stroke="var(--cyan)"/><path d="M24 58h16M32 46v12" stroke="var(--navy)"/><rect x="68" y="2" width="18" height="56" rx="2" stroke="var(--navy)"/><path d="M72 12h10M72 20h10" stroke="var(--cyan)"/></svg>
  Desktop<br><span>Applications</span>
</div>

<!-- Welcome -->
<h1 class="section-title display" style="top:963px">Welcome to <span class="c-navy">Brightwell</span> <span class="c-cyan">Systems</span></h1>
<p class="lead" style="top:1022px">Sed ut perspiciatis unde omnis iste natus error sit voluptatem accusantium doloremque laudantium, totam rem aperiam, eaque ipsa quae ab illo inventore veritatis et quasi architecto beatae vitae dicta sunt explicabo. Nemo enim ipsam voluptatem quia voluptas sit aspernatur aut odit aut fugit, sed quia consequuntur magni dolores eos qui ratione voluptatem sequi nesciunt.</p>
<div class="btn btn-cyan" style="left:386px;top:1152px;width:205px">Read More <svg viewBox="0 0 20 20"><circle cx="10" cy="10" r="10" fill="#fff"/><path d="M6 10h7M10 6l4 4-4 4" stroke="var(--cyan)" stroke-width="2.4" fill="none"/></svg></div>
<div class="btn btn-navy" style="left:608px;top:1152px;width:206px">Contact Us <svg viewBox="0 0 20 20"><circle cx="10" cy="10" r="10" fill="#fff"/><path d="M6 10h7M10 6l4 4-4 4" stroke="var(--navy)" stroke-width="2.4" fill="none"/></svg></div>
<div class="abs divider"></div>

<!-- Focus areas -->
<div class="ring" style="left:80px;top:1368px;width:444px;height:444px">
  <div class="photo" role="img" aria-label="Developer writing code at a laptop with monitors" style="background:linear-gradient(135deg,#d9dde3 0%,#6b7480 45%,#1d2330 100%)"></div>
</div>
<h2 class="abs focus-title display">Our Main <span class="c-navy">Focus</span> <span class="c-cyan">Areas</span></h2>
<p class="abs focus-text">Sed ut perspiciatis unde omnis iste natus error sit voluptatem doloremque laudantium, totam rem aperiam explicabo</p>
<ul class="abs focus-list">
  <li><svg width="16" height="16" viewBox="0 0 20 20"><circle cx="10" cy="10" r="8.5" fill="none" stroke="var(--navy)" stroke-width="2"/><path d="M6 10h7M10 7l3 3-3 3" stroke="var(--navy)" stroke-width="2" fill="none"/></svg>Software Development</li>
  <li><svg width="16" height="16" viewBox="0 0 20 20"><circle cx="10" cy="10" r="8.5" fill="none" stroke="var(--navy)" stroke-width="2"/><path d="M6 10h7M10 7l3 3-3 3" stroke="var(--navy)" stroke-width="2" fill="none"/></svg>Web Applications</li>
  <li><svg width="16" height="16" viewBox="0 0 20 20"><circle cx="10" cy="10" r="8.5" fill="none" stroke="var(--navy)" stroke-width="2"/><path d="M6 10h7M10 7l3 3-3 3" stroke="var(--navy)" stroke-width="2" fill="none"/></svg>Desktop Applications</li>
  <li><svg width="16" height="16" viewBox="0 0 20 20"><circle cx="10" cy="10" r="8.5" fill="none" stroke="var(--navy)" stroke-width="2"/><path d="M6 10h7M10 7l3 3-3 3" stroke="var(--navy)" stroke-width="2" fill="none"/></svg>Mobile Applications</li>
</ul>
<div class="btn btn-cyan" style="left:583px;top:1698px;width:205px">Read More <svg viewBox="0 0 20 20"><circle cx="10" cy="10" r="10" fill="#fff"/><path d="M6 10h7M10 6l4 4-4 4" stroke="var(--cyan)" stroke-width="2.4" fill="none"/></svg></div>

<!-- What we do -->
<section class="abs band" role="img" aria-label="Blue background with faint lines of program code"></section>
<svg class="abs" style="left:0;top:1890px" width="1200" height="80" viewBox="0 0 1200 80">
  <path d="M0 0H1200V5Q600 75 0 5Z" fill="#fff"/>
  <path d="M110 20Q600 80 1090 20" fill="none" stroke="#fff" stroke-width="4"/>
</svg>
<svg class="abs" style="left:0;top:2565px" width="1200" height="82" viewBox="0 0 1200 82">
  <path d="M0 82V72Q600 -20 1200 72V82Z" fill="#fff"/>
  <path d="M150 40Q600 -10 1050 40" fill="none" stroke="var(--cyan)" stroke-width="4"/>
</svg>
<h2 class="abs wwd-title display">What We Do</h2>
<p class="abs wwd-text">Sed ut perspiciatis unde omnis iste natus error sit voluptatem accusantium doloremque laudantium, totam rem aperiam, eaque ipsa quae ab illo inventore veritatis et quasi architecto beatae vitae dicta sunt explicabo. Nemo enim ipsam voluptatem quia voluptas sit aspernatur aut odit aut fugit, sed quia consequuntur magni dolores eos qui ratione voluptatem sequi nesciunt.</p>
<div class="btn btn-navy" style="left:90px;top:2357px;width:204px">Our Services <svg viewBox="0 0 20 20"><circle cx="10" cy="10" r="10" fill="#fff"/><path d="M6 10h7M10 6l4 4-4 4" stroke="var(--navy)" stroke-width="2.4" fill="none"/></svg></div>
<div class="ring" style="left:690px;top:2045px;width:446px;height:446px;background:#fff;border-color:var(--cyan)">
  <div class="photo" role="img" aria-label="Hands holding a smartphone surrounded by app development icons" style="background:linear-gradient(140deg,#f2f3f5 0%,#8a8f98 45%,#1b1c20 100%)"></div>
</div>

<!-- Blog -->
<h2 class="section-title display" style="top:2725px">Our <span class="c-navy">Blog</span></h2>
<article class="card" style="left:90px">
  <div class="img" role="img" aria-label="Person working at a desktop computer" style="background:linear-gradient(135deg,#2b2f36,#8d939b)"><span class="date">Aug 17 2018</span></div>
  <h3>SED UT PERSPICIATIS UND</h3>
  <p>Sed ut perspiciatis unde omnis iste natus error sit voluptatem accusantium doloremque laudantium, totam rem aperiam, eaque ipsa quae ab illo</p>
  <a>READ MORE</a>
</article>
<article class="card" style="left:436px">
  <div class="img" role="img" aria-label="Screens displaying responsive web layouts" style="background:linear-gradient(135deg,#e8f2fa,#3d8fd0)"><span class="date">Aug 17 2018</span></div>
  <h3>SED UT PERSPICIATIS UND</h3>
  <p>Sed ut perspiciatis unde omnis iste natus error sit voluptatem accusantium doloremque laudantium, totam rem aperiam, eaque ipsa quae ab illo</p>
  <a>READ MORE</a>
</article>
<article class="card" style="left:780px">
  <div class="img" role="img" aria-label="Programmer at a desk with code on monitors" style="background:linear-gradient(135deg,#a7b0b8,#1e2630)"><span class="date">Aug 17 2018</span></div>
  <h3>SED UT PERSPICIATIS UND</h3>
  <p>Sed ut perspiciatis unde omnis iste natus error sit voluptatem accusantium doloremque laudantium, totam rem aperiam, eaque ipsa quae ab illo</p>
  <a>READ MORE</a>
</article>

<!-- Clients -->
<h2 class="section-title display" style="top:3233px">Our <span class="c-cyan">Clients</span></h2>
<p class="lead" style="top:3288px;line-height:33px;font-size:15.5px">Lorem ipsum dolor sit amet, consectetur adipiscing do eiusmod tempor incididunt ut labore et dolore magna. Ut enim ad minim veniam, quis nostrud exercitation ullamco</p>
<span class="arrow" style="left:16px">&#8249;</span>
<div class="client" style="left:90px"><i></i>Northbore</div>
<div class="client" style="left:297px">Harbourline</div>
<div class="client active" style="left:504px">Keystone Build</div>
<div class="client" style="left:712px">Corvant</div>
<div class="client" style="left:919px"><i></i>Ashford Bridge</div>
<span class="arrow" style="left:1168px">&#8250;</span>

<!-- Contact -->
<h2 class="section-title display" style="top:3537px">Contact <span class="c-navy">Us</span></h2>
<p class="abs" style="left:0;top:3594px;width:1200px;text-align:center;font-size:16.5px;color:var(--ink)">Contact us for more information</p>
<div class="field" style="left:161px;top:3648px;width:430px">&#128100; First Name</div>
<div class="field" style="left:609px;top:3648px;width:430px">&#128100; Last Name</div>
<div class="field" style="left:161px;top:3703px;width:430px">&#9638; Company</div>
<div class="field" style="left:161px;top:3758px;width:430px">&#9993; Email Address</div>
<div class="field" style="left:161px;top:3812px;width:430px">&#9990; Phone Number</div>
<div class="field msg" style="left:609px;top:3703px;width:430px;height:149px">&#9998; Message :</div>
<div class="btn btn-cyan" style="left:498px;top:3866px;width:206px;font-size:17px"><svg viewBox="0 0 20 20"><path d="M2 9l16-7-5 16-3-6z" fill="#fff"/></svg>Submit</div>

<!-- Footer -->
<footer class="abs footer"></footer>
<svg class="abs" style="left:0;top:3996px" width="1200" height="110" viewBox="0 0 1200 110">
  <path d="M0 0H1200V8Q600 80 0 8Z" fill="#fff"/>
  <path d="M280 40Q600 85 920 40" fill="none" stroke="var(--cyan)" stroke-width="3"/>
  <circle cx="600" cy="70" r="26" fill="#fff" stroke="var(--cyan)" stroke-width="3"/>
</svg>
<div class="abs" style="left:545px;top:4150px;width:110px;height:110px;border-radius:50%;background:var(--cyan)"></div>
<div class="abs foot-name display"><span class="c-navy">Brightwell</span> <span class="c-cyan">Systems</span></div>
<div class="foot-icon" style="left:259px"><svg width="40" height="40" viewBox="0 0 24 24" fill="none" stroke="#fff" stroke-width="1.6"><path d="M12 22s7-7 7-12a7 7 0 0 0-14 0c0 5 7 12 7 12z"/><circle cx="12" cy="10" r="2.5"/></svg></div>
<div class="foot-icon" style="left:565px"><svg width="40" height="40" viewBox="0 0 24 24" fill="none" stroke="#fff" stroke-width="1.6"><path d="M6.6 10.8a15 15 0 0 0 6.6 6.6l2.2-2.2c.3-.3.7-.4 1-.2 1.1.4 2.3.6 3.6.6.6 0 1 .4 1 1V20c0 .6-.4 1-1 1A17 17 0 0 1 3 4c0-.6.4-1 1-1h3.5c.6 0 1 .4 1 1 0 1.3.2 2.5.6 3.6.1.3 0 .7-.2 1z"/></svg></div>
<div class="foot-icon" style="left:869px"><svg width="40" height="40" viewBox="0 0 24 24" fill="none" stroke="#fff" stroke-width="1.6"><rect x="3" y="5" width="18" height="14" rx="1"/><path d="M3 6l9 7 9-7M3 19l7-6M21 19l-7-6"/></svg></div>

</body>
</html>
```